continuing medical education travel company. luxury, professional, quality service

PLEASE USE THE REVISED LOGO FOR ALL CARD DESIGNS, NO SNAKE HEAD

Target Market(s)

physicians

Industry/Entity Type

Travel Industry

Contact Information for Business Card

luxury quality, spot uv, foil, rounded corners

Colors
0255a3
3176b5
cfdeed
aaaaaa
5c5c5c

Requirements
Must have
• navy, platinum, possible holographic

```html
<!DOCTYPE html>
<html lang="en">
<head>
<meta charset="utf-8">
<title>Veridia Travel – Business Card</title>
<link rel="stylesheet" href="https://fonts.googleapis.com/css2?family=Open+Sans:wght@400;600&display=swap">
<style>
  :root {
    --backdrop: #141414;
    --card: #ffffff;
    --navy: #2a2f8c;
    --ink: #1c1c1c;
    --rule: #aaaaaa;
    --pattern-light: #f1f1f8;
    --pattern-tone: #e2e2ef;
  }
  * { margin: 0; padding: 0; box-sizing: border-box; }
  html, body {
    width: 1200px;
    height: 900px;
    overflow: hidden;
    background: var(--backdrop);
    font-family: "Open Sans", Arial, sans-serif;
  }
  .stage { position: relative; width: 1200px; height: 900px; }
  .card {
    position: absolute;
    top: 170px;
    width: 347px;
    height: 561px;
    background: var(--card);
    overflow: hidden;
  }
  .card--front { left: 259px; }
  .card--back { left: 631px; }

  .holder {
    position: absolute;
    top: 236px;
    width: 100%;
    text-align: center;
    margin-top: -170px;
  }
  .holder__name {
    font-weight: 600;
    font-size: 19px;
    color: var(--navy);
    line-height: 26px;
  }
  .holder__role {
    font-size: 15px;
    color: var(--ink);
    line-height: 20px;
  }

  .wordmark {
    position: absolute;
    width: 100%;
    text-align: center;
    font-weight: 600;
    color: var(--navy);
    line-height: 1.1;
  }
  .card--front .wordmark { top: 190px; font-size: 36px; }
  .card--back .wordmark { top: 345px; font-size: 40px; }
  .wordmark span { display: block; font-size: 0.6em; letter-spacing: 0.5em; padding-left: 0.5em; }

  .contact {
    position: absolute;
    top: 385px;
    width: 100%;
    text-align: center;
    font-size: 15px;
    line-height: 20px;
    color: var(--ink);
  }
  .contact__rule {
    width: 90px;
    height: 1px;
    background: var(--rule);
    margin: 11px auto 15px;
  }

  .card__pattern {
    position: absolute;
    inset: 0;
    background: linear-gradient(160deg, var(--pattern-light), var(--pattern-tone) 50%, var(--pattern-light));
  }
</style>
</head>
<body>
<main class="stage">
  <section class="card card--front">
    <div class="holder">
      <p class="holder__name">Maren Holt</p>
      <p class="holder__role">Principal</p>
    </div>
    <p class="wordmark">VERIDIA<span>TRAVEL</span></p>
    <div class="contact">
      <p>514.555.0187</p>
      <p>veridiatravel.com</p>
      <p>mholt@veridiatravel.com</p>
      <div class="contact__rule"></div>
      <p>48, Harbour Ave, Lakeview,</p>
      <p>QC H0H 0H0</p>
    </div>
  </section>

  <section class="card card--back">
    <div class="card__pattern" role="img" aria-label="Faint repeating lavender brand-name pattern across the card back"></div>
    <p class="wordmark">VERIDIA<span>TRAVEL</span></p>
  </section>
</main>
</body>
</html>
```